"The Wandering Mentor", a Higher Ed blogger, would like a wordpress design

I would like a wordpress design for blogs written by "The Wandering Mentor." that can be easily expanded by me once the initial design is complete.

Here is context which I would like included on the Home/Welcome page: "I started The Wandering Mentor in 2021 to write about the practice of academic advising through the lens of horsemanship. After one year of developing skills as a brand new equestrian, I couldn’t help but notice the similarities between my vocation as an academic advisor and my avocation as a budding equestrian. I hope my musings about my journey in two very different fields will cultivate curiosity, widen your aperture and ignite academic advisors to take their practice to the next level. "

The wordpress will primarily have blogs by myself or guest bloggers writing about academic advising for advisors, but I may widen my audience to include students and families. I'd like to have readers submit questions that I can answer. Depending on interest, I may want to have a section on Horsemanship but that is not truly the focus of this site.

I'd like the feel of the site to be positive, fresh, modern (but not too wild), with the emphasis on Higher Ed/Academic Advising as opposed to equestrian pursuits. I don't want it to feel clunky and blocky like some sites that have to do with education. I'm hoping that readers will have some "aha" moments after reading some of the posts.

I have included my logo files

```html
<!DOCTYPE html>
<html lang="en">
<head>
<meta charset="utf-8">
<title>The Wandering Mentor – Blog</title>
<link rel="stylesheet" href="https://fonts.googleapis.com/css2?family=Mulish:wght@400;500;600;700&family=Roboto+Condensed:wght@400&display=swap">
<style>
:root{
  --black:#000;
  --panel:#171717;
  --band:#1b1b1b;
  --footer:#121212;
  --gold:#d1a35c;
  --gold-soft:#b08c5a;
  --gold-fill:#ddb068;
  --white:#fff;
  --text:#e6e6e6;
  --muted:#a3a3a3;
  --tag:#333;
  --input:#4a4a4a;
  --ad:#cbcbcb;
  --line:#333;
}
*{box-sizing:border-box;margin:0;padding:0}
html,body{width:1200px;height:3876px;overflow:hidden;background:var(--black)}
body{position:relative;font-family:'Mulish',sans-serif;color:var(--text)}
.abs{position:absolute}
.photo{position:absolute}
.btn{position:absolute;border:1.5px solid var(--gold);color:var(--gold);font-size:13px;font-weight:600;display:flex;align-items:center;justify-content:center;height:36px;width:106px}
.date{position:absolute;color:var(--gold);font-size:13px;font-weight:600}
.post-title{position:absolute;color:var(--white);font-size:19px;line-height:23px;font-weight:400}
.excerpt{position:absolute;color:var(--muted);font-size:12.5px;line-height:21.5px}
/* header */
.hero{position:absolute;left:0;top:0;width:1200px;height:600px;background:linear-gradient(100deg,#2c3138 0%,#4b4c4f 35%,#5d5a56 55%,#3a3633 80%,#24201e 100%)}
.hero-shade{position:absolute;inset:0;background:rgba(0,0,0,.35)}
.main-nav{position:absolute;top:16px;left:163px;display:flex;gap:0;font-size:13px}
.main-nav a{color:var(--gold);text-decoration:none;position:absolute;white-space:nowrap}
.main-nav a.current{color:var(--white)}
.social{position:absolute;display:flex;gap:11px}
.social span{width:24px;height:24px;border:1.5px solid var(--gold);border-radius:50%;display:block}
.brand{position:absolute;left:450px;top:120px;width:300px;height:240px;display:flex;flex-direction:column;align-items:center;justify-content:center;gap:14px}
.brand .dot{width:18px;height:18px;border:2px solid var(--gold);border-radius:50%}
.brand .name{font-size:30px;font-weight:600;color:var(--gold);text-align:center;line-height:36px}
.hero-title{position:absolute;top:390px;left:0;width:1200px;text-align:center;font-family:'Roboto Condensed',sans-serif;font-size:41px;line-height:50px;color:var(--white)}
/* sidebar */
.widget{position:absolute;left:769px;width:270px;background:var(--panel);padding:0 16px}
.widget h3{font-size:18px;font-weight:500;color:var(--text)}
.widget .rule{width:58px;height:2px;background:var(--gold);margin-top:10px}
.tags{display:flex;flex-wrap:wrap;gap:8px 8px;margin-top:18px;width:240px}
.tags span{background:var(--tag);color:var(--text);font-size:12px;padding:4px 10px}
.recent li{list-style:none;position:relative;padding-left:18px;color:var(--muted);font-size:11.5px;line-height:16px;margin-bottom:13px}
.recent li::before{content:"";position:absolute;left:0;top:6px;width:4px;height:4px;background:var(--gold);border-radius:50%}
.input{background:var(--input);color:#bbb;font-size:11px;display:flex;align-items:center;padding-left:12px;position:absolute}
</style>
</head>
<body>

<header class="hero">
  <div class="photo" role="img" aria-label="Photo of an academic advisor meeting with a student" style="inset:0;background:linear-gradient(100deg,#2c3138 0%,#4b4c4f 35%,#5d5a56 55%,#3a3633 80%,#24201e 100%)"></div>
  <div class="hero-shade"></div>
  <nav class="main-nav">
    <a class="current" style="left:0">Home</a>
    <a style="left:69px">Academic Topics</a>
    <a style="left:207px">Coaching</a>
    <a style="left:298px">About</a>
    <a style="left:367px">Horsemanship</a>
  </nav>
  <div class="social" style="left:906px;top:12px"><span></span><span></span><span></span><span></span></div>
  <div class="brand"><span class="dot"></span><div class="name">The Wandering<br>Mentor</div></div>
  <h1 class="hero-title" style="font-weight:400">Providing Academic Advising Through The<br>Lens of Horsemanship</h1>
</header>

<main>
  <!-- featured -->
  <div class="photo" role="img" aria-label="White horse standing among autumn trees" style="left:161px;top:713px;width:441px;height:361px;background:linear-gradient(135deg,#2e3a1c,#7a5a23 45%,#c9b8a0 60%,#3a2a14)"></div>
  <div class="date" style="left:632px;top:771px">January 29, 2021</div>
  <h2 class="post-title" style="left:632px;top:796px;font-size:24px;line-height:29px;width:420px">Lorem Ipsum Dolor Sit Amet, Cons Ctetuer Adipiscing Elit</h2>
  <p class="excerpt" style="left:632px;top:860px;width:395px">Lorem ipsum dolor sit amet, consectetuer adipiscing elit, sed diam nonummy nibh euismod tincidunt ut laoreet ore magna aliquam erat volutpat. Ut wisi enim ad minim veniam, quis nostrud exerci tation ullamcorper suscipit lobortis nisl ut aliquip ex ea commodo consequat.</p>
  <a class="btn" style="left:632px;top:977px">Read More</a>

  <!-- post 1 -->
  <div class="photo" role="img" aria-label="Woman sitting in the grass beside a resting horse" style="left:161px;top:1148px;width:270px;height:195px;background:linear-gradient(160deg,#7c9a3a,#a4bb56 40%,#6b3e22 60%,#6e8b34)"></div>
  <div class="date" style="left:454px;top:1153px">January 29, 2021</div>
  <h2 class="post-title" style="left:454px;top:1176px;width:260px">Lorem Ipsum Dolor Sit Met, Cons Ctetuer Adipisci.</h2>
  <p class="excerpt" style="left:454px;top:1228px;width:245px">Lorem ipsum dolor sit amet, ectetuer adipiscing elit, sed diam nonummy nibh euismod tincidunt ut lao.</p>
  <a class="btn" style="left:454px;top:1302px">Read More</a>

  <!-- wide feature -->
  <div class="photo" role="img" aria-label="Advisor and student looking at a laptop together" style="left:161px;top:1386px;width:563px;height:357px;background:linear-gradient(180deg,#c9d0d6 0%,#8e97a4 45%,#3d4450 80%,#0c0c0c 100%)"></div>
  <h2 class="abs" style="left:161px;top:1680px;width:548px;text-align:center;font-size:23px;line-height:29px;font-weight:400;color:var(--white)">Lorem Ipsum Dolor Sit Amens Ctetuer<br>Adipiscing Elit</h2>

  <!-- post 2 -->
  <div class="photo" role="img" aria-label="Two colleagues talking in an office" style="left:163px;top:1787px;width:268px;height:195px;background:linear-gradient(135deg,#c9cdd1,#8c96a4 45%,#3e4c6c 60%,#e5e3df)"></div>
  <div class="date" style="left:455px;top:1795px">January 29, 2021</div>
  <h2 class="post-title" style="left:455px;top:1818px;width:260px">Lorem Ipsum Dolor Sit Met, Cons Ctetuer Adipisci.</h2>
  <p class="excerpt" style="left:455px;top:1870px;width:245px">Lorem ipsum dolor sit amet, ectetuer adipiscing elit, sed diam nonummy nibh euismod tincidunt ut lao.</p>
  <a class="btn" style="left:455px;top:1944px">Read More</a>

  <!-- cards -->
  <div class="photo" role="img" aria-label="Rider jumping a horse over a fence at a show" style="left:160px;top:2017px;width:269px;height:195px;background:linear-gradient(180deg,#5f97d4 0%,#9bc2ea 35%,#8a8f84 50%,#7b6b4e 75%,#b9bcbf 100%)"></div>
  <div class="date" style="left:163px;top:2232px">January 29, 2021</div>
  <h2 class="post-title" style="left:163px;top:2256px;width:260px">Lorem Ipsum Dolor Sit Met, Cons Ctetuer Adipisci.</h2>
  <p class="excerpt" style="left:163px;top:2308px;width:245px">Lorem ipsum dolor sit amet, ectetuer adipiscing elit, sed diam nonummy nibh euismod tincidunt ut lao.</p>
  <a class="btn" style="left:163px;top:2381px">Read More</a>

  <div class="photo" role="img" aria-label="Group of students working together at a table" style="left:464px;top:2017px;width:270px;height:195px;background:linear-gradient(135deg,#e6e8e6,#b9c4c7 40%,#8a6a55 65%,#d9d6d0)"></div>
  <div class="date" style="left:464px;top:2232px">January 29, 2021</div>
  <h2 class="post-title" style="left:464px;top:2256px;width:260px">Lorem Ipsum Dolor Sit Met, Cons Ctetuer Adipisci.</h2>
  <p class="excerpt" style="left:464px;top:2308px;width:245px">Lorem ipsum dolor sit amet, ectetuer adipiscing elit, sed diam nonummy nibh euismod tincidunt ut lao.</p>
  <a class="btn" style="left:464px;top:2381px">Read More</a>

  <a class="btn" style="left:361px;top:2481px">Load More</a>

  <!-- sidebar -->
  <aside>
    <section class="widget" style="top:1153px;height:219px;padding-top:24px">
      <h3>Subscribe To Our Blog</h3><div class="rule"></div>
      <p style="color:var(--muted);font-size:12px;line-height:19px;margin-top:15px;width:230px">Get the latest tips &amp; updates right to your inbox</p>
      <div class="input" style="left:16px;top:127px;width:237px;height:35px">Enter Your email</div>
      <a class="btn" style="left:16px;top:173px;width:90px;height:32px">Subscribe</a>
    </section>
    <section class="widget" style="top:1398px;height:129px;padding-top:27px;padding-left:18px">
      <h3>Follow Us On</h3><div class="rule"></div>
      <div class="social" style="left:18px;top:78px;gap:9px"><span></span><span></span><span></span><span></span></div>
    </section>
    <section class="widget" style="top:1553px;height:270px;padding-top:27px;padding-left:18px">
      <h3>Follow Us On</h3><div class="rule"></div>
      <div class="tags">
        <span>Lorem</span><span>Lorem Ipsu</span><span>Rem Ipsu</span>
        <span>Lorem Ipsu</span><span>Rem Ipsu</span><span>Lorm Dol</span>
        <span>Lorem Ipsu</span><span>Rem Ipsu</span><span>Lorem Ol</span>
        <span>Lorem Ipsm Do</span><span>Rem Ipsu</span>
        <span>Lorem</span><span>Lorem Ipsu</span><span>Rem Ipsu</span>
      </div>
    </section>
    <section class="widget" style="top:1855px;height:260px;padding-top:29px">
      <h3>Recent Posts</h3><div class="rule"></div>
      <svg class="abs" style="left:233px;top:32px" width="22" height="14" viewBox="0 0 22 14" fill="none" stroke="var(--gold)" stroke-width="1.5"><path d="M7 2 2 7l5 5M15 2l5 5-5 5"/></svg>
      <ul class="recent" style="margin-top:18px;width:235px">
        <li>Lorem ipsum dolor sit amctetuer atc ng elit, sed diam nonummy.</li>
        <li>Lorem ipsum dolor sit amctetuer atc ng elit, sed diam nonummy.</li>
        <li>Lorem ipsum dolor sit amctetuer atc ng elit, sed diam nonummy.</li>
        <li>Lorem ipsum dolor sit amctetuer atc ng elit, sed diam nonummy.</li>
      </ul>
    </section>
    <section class="abs" style="left:769px;top:2149px;width:270px;height:270px;background:var(--ad);text-align:center;color:#8a8a8a">
      <div style="margin-top:105px;font-size:18px">Your AD Here</div>
      <div style="width:128px;height:1px;background:#999;margin:8px auto 0"></div>
      <div style="margin-top:10px;font-size:18px;color:#777">SIZE: 360 x 360</div>
    </section>
  </aside>
</main>

<section class="abs" style="left:0;top:2605px;width:1200px;height:203px;background:var(--band)">
  <svg class="abs" style="left:348px;top:40px" width="112" height="115" viewBox="0 0 112 115" fill="none" stroke="var(--gold-soft)" stroke-width="3" stroke-linejoin="round">
    <path d="M4 45 56 8l52 37v66H4z"/><path d="M4 45l52 38 52-38"/><path d="M4 111l40-36M108 111 68 75"/>
    <rect x="24" y="24" width="64" height="42" fill="var(--band)"/><path d="M38 36h36M38 46h36M38 56h24"/>
  </svg>
  <h2 class="abs" style="left:487px;top:45px;font-size:30px;font-weight:400;color:var(--white)">Subscribe To Our Blog</h2>
  <p class="abs" style="left:489px;top:90px;font-size:15px;color:var(--text)">Get the latest tips &amp; updates right to your inbox</p>
  <div class="input" style="left:485px;top:117px;width:248px;height:35px;background:#d5d5d5;color:#555">Enter Your email</div>
  <div class="abs" style="left:733px;top:117px;width:92px;height:35px;background:var(--gold-fill);color:#222;font-size:13px;display:flex;align-items:center;justify-content:center">Subscribe</div>
</section>

<section class="abs" style="left:0;top:2808px;width:1200px;height:626px;background:var(--black)">
  <div class="abs" style="left:591px;top:38px;width:18px;height:18px;border:2px solid var(--gold);border-radius:50%"></div>
  <h2 class="abs" style="left:0;top:80px;width:1200px;text-align:center;font-size:24px;font-weight:400;color:var(--white)">About The Wandering Mentor</h2>
  <div class="photo" role="img" aria-label="Woman hugging a brown and white horse" style="left:161px;top:162px;width:440px;height:363px;background:linear-gradient(120deg,#4c6a2c,#7d8f4a 35%,#8a5a34 55%,#d9d0c4 70%,#3a3a2a)"></div>
  <h3 class="abs" style="left:628px;top:190px;font-weight:400;color:var(--gold-soft);font-size:28px">Clara Whitfield, <span style="font-size:17px">Wandering Mentor</span></h3>
  <p class="abs" style="left:630px;top:242px;width:390px;font-size:15.5px;line-height:23px;color:var(--white)">I started The Wandering Mentor in 2021 to write about the practice of academic advising through the lens of horsemanship</p>
  <p class="excerpt" style="left:630px;top:322px;width:410px;color:#b5b5b5">After one year of developing skills as a brand new equestrian, I couldn’t help but notice the similarities between my vocation as an academic advisor and my avocation as a budding equestrian. I hope my musings about my journey in two very different fields will cultivate curiosity, widen your aperture and ignite academic advisors to take their practice to the next level.</p>
  <a class="btn" style="left:630px;top:469px;width:153px">Contact Me Today</a>
</section>

<footer class="abs" style="left:0;top:3434px;width:1200px;height:442px;background:var(--footer)">
  <div class="abs" style="left:450px;top:58px;width:300px;display:flex;flex-direction:column;align-items:center;gap:10px">
    <span style="width:14px;height:14px;border:2px solid var(--gold);border-radius:50%"></span>
    <span style="color:var(--gold);font-size:20px;font-weight:600;text-align:center;line-height:25px">The Wandering<br>Mentor</span>
  </div>
  <nav class="main-nav" style="top:208px;left:370px">
    <a class="current" style="left:0">Home</a>
    <a style="left:69px">Academic Topics</a>
    <a style="left:206px">Coaching</a>
    <a style="left:297px">About</a>
    <a style="left:366px">Horsemanship</a>
  </nav>
  <div class="abs" style="left:161px;top:246px;width:878px;height:1px;background:var(--line)"></div>
  <svg class="abs" style="left:185px;top:286px" width="46" height="46" viewBox="0 0 46 46" fill="none" stroke="var(--gold-soft)" stroke-width="1.5"><circle cx="23" cy="23" r="22"/><path d="M17 14c-2 1-3 3-2 6 2 5 6 9 11 11 3 1 5 0 6-2l-3-3-3 2c-3-1-5-4-6-6l2-3z"/></svg>
  <div class="abs" style="left:242px;top:290px;font-size:13px;line-height:22px;color:var(--white)">PHONE<br>&nbsp;555-014-2290</div>
  <svg class="abs" style="left:431px;top:286px" width="46" height="46" viewBox="0 0 46 46" fill="none" stroke="var(--gold-soft)" stroke-width="1.5"><circle cx="23" cy="23" r="22"/><path d="M23 33s-7-7-7-12a7 7 0 0 1 14 0c0 5-7 12-7 12z"/><circle cx="23" cy="21" r="2.5"/></svg>
  <div class="abs" style="left:495px;top:290px;font-size:13px;line-height:22px;color:var(--white)">Lorem ipsum dolor sit amet, ectetuer<br>adipiscing elit, sed diam nonu.</div>
  <svg class="abs" style="left:817px;top:286px" width="46" height="46" viewBox="0 0 46 46" fill="none" stroke="var(--gold-soft)" stroke-width="1.5"><circle cx="23" cy="23" r="22"/><path d="M14 20l9-6 9 6v11H14zM14 20l9 6 9-6"/></svg>
  <div class="abs" style="left:882px;top:290px;font-size:13px;line-height:20px;color:var(--white)">EMAIL<br>hello@wanderingmentor.blog</div>
  <div class="abs" style="left:161px;top:372px;width:878px;height:1px;background:var(--line)"></div>
  <p class="abs" style="left:0;top:403px;width:1200px;text-align:center;font-size:13px;color:var(--white)">Copyright © 2021 The Wandering Mentor. All Rights Reserved.</p>
</footer>

</body>
</html>
```